Visitenkarten-Design für Hotel und Restaurant in der Fußgängerzone
Zielgruppe
Hotel und Restaurant in der Fußgängerzone, zwei Gehminuten zum Bodensee.
Neu renoviertes Hotel/Restaurant (z.B.Boxspringbett, Holzboden, USB Steckdosen).
Übernachtung mit Frühstück im Einzel,-Doppel,- oder Komfortzimmer (für 3 Personen).
Restaurant mit regionaler Küche. Besondere saisonale Zutaten unserer Nachbarländer als Specials.
Touristen im Sommer Durchschnittalter: 50 Jahre, sportlich, modern, gut betucht.
Einwohner der Stadt im Winter, Alter zwischen 25 und 65 Jahre, viele davon Hausbesitzer, Segelboot Besitzer etc.
Aufgabenstellung
Farbkonzept im Restaurant:
warm- weiße Wände, dunkle Holzmöbel, rote Barelemente, weiß-kupferfarbene Lampen.
Würden uns etwas minimalistisches wünschen, trotzdem mit einem Wow Effekt.
Sei es ein ausgeschnittenes Logo, abgerundete Ecken, besonderes Material usw.
Dateianhänge sind nur für´s bessere Verständnis, muss nicht zwingend als Vorgabe gesehen werden.
Vorderseite:
Logo
Hotel & Restaurant (kann, muss aber nicht draufstehen.)
zum Anker
Seedorf

```html
<!DOCTYPE html>
<html lang="de">
<head>
<meta charset="utf-8">
<title>zum Anker – Visitenkarte</title>
<link rel="stylesheet" href="https://fonts.googleapis.com/css2?family=Jost:wght@300;400&display=swap">
<style>
  :root {
    --stage: #ece9e6;
    --card-red: #9e2620;
    --card-frame: #ffffff;
    --ink-light: #ffffff;
    --ink-soft: rgba(255, 255, 255, 0.82);
    --mark-fill: rgba(255, 255, 255, 0.9);
    --cutout: #3a1a14;
  }
  * { box-sizing: border-box; margin: 0; padding: 0; }
  html, body {
    width: 1200px;
    height: 758px;
    overflow: hidden;
    background: var(--stage);
    font-family: "Jost", "Helvetica Neue", Arial, sans-serif;
  }
  .canvas {
    position: relative;
    width: 1200px;
    height: 758px;
    display: flex;
    align-items: center;
    justify-content: center;
    gap: 60px;
  }
  .card {
    position: relative;
    width: 520px;
    height: 336px;
    background: var(--card-red);
    border: 7px solid var(--card-frame);
    border-radius: 14px 56px 14px 56px;
    color: var(--ink-light);
    overflow: hidden;
    box-shadow: 0 10px 28px rgba(60, 20, 15, 0.18);
  }

  /* Front */
  .card-front {
    display: flex;
    flex-direction: column;
    align-items: center;
    justify-content: center;
  }
  .brand-dot {
    width: 100px;
    height: 100px;
    border-radius: 50%;
    background: var(--mark-fill);
    margin-bottom: 34px;
  }
  .brand-name {
    font-weight: 400;
    font-size: 38px;
    line-height: 1;
    letter-spacing: 0.5px;
  }
  .brand-place {
    display: flex;
    align-items: center;
    gap: 10px;
    margin-top: 10px;
    font-weight: 300;
    font-size: 13px;
    letter-spacing: 1.5px;
    color: var(--ink-soft);
  }
  .brand-place::before,
  .brand-place::after {
    content: "";
    width: 30px;
    height: 1px;
    background: var(--ink-soft);
  }

  /* Back */
  .card-back .back-dot {
    position: absolute;
    top: 50px;
    left: 50%;
    width: 104px;
    height: 104px;
    margin-left: -52px;
    border-radius: 50%;
    background: var(--cutout);
  }
  .card-back .contact-name {
    position: absolute;
    left: 60px;
    top: 168px;
    font-weight: 300;
    font-size: 19px;
  }
  .contact-list {
    position: absolute;
    left: 36px;
    right: 30px;
    top: 214px;
    display: grid;
    grid-template-columns: 1fr 1fr;
    row-gap: 20px;
    column-gap: 20px;
    list-style: none;
    font-weight: 300;
    font-size: 13px;
    line-height: 1.3;
  }
  .contact-item {
    display: flex;
    align-items: flex-start;
    gap: 9px;
  }
  .contact-item svg {
    flex: 0 0 15px;
    width: 15px;
    height: 15px;
    margin-top: 1px;
  }
  .contact-item.is-offset { margin-top: 14px; }
</style>
</head>
<body>
<main class="canvas">

  <section class="card card-front" aria-label="Vorderseite">
    <span class="brand-dot" aria-hidden="true"></span>
    <h1 class="brand-name">zum Anker</h1>
    <p class="brand-place">Seedorf</p>
  </section>

  <section class="card card-back" aria-label="Rückseite">
    <span class="back-dot" aria-hidden="true"></span>
    <h2 class="contact-name">Zum Anker</h2>
    <ul class="contact-list">
      <li class="contact-item">
        <svg viewBox="0 0 16 16" aria-hidden="true"><circle cx="8" cy="8" r="8" fill="#fff"/><path d="M8 3.2a3 3 0 0 0-3 3c0 2.2 3 6 3 6s3-3.8 3-6a3 3 0 0 0-3-3zm0 4.1a1.1 1.1 0 1 1 0-2.2 1.1 1.1 0 0 1 0 2.2z" fill="#9e2620"/></svg>
        <span>Seestraße 12<br>78120 Seedorf</span>
      </li>
      <li class="contact-item is-offset">
        <svg viewBox="0 0 16 16" aria-hidden="true"><circle cx="8" cy="8" r="8" fill="#fff"/><rect x="4" y="5" width="8" height="6" rx="1" fill="none" stroke="#9e2620" stroke-width="1.1"/><path d="M4.3 5.4 8 8.3l3.7-2.9" fill="none" stroke="#9e2620" stroke-width="1.1"/></svg>
        <span>info@zum-anker-seedorf.de</span>
      </li>
      <li class="contact-item">
        <svg viewBox="0 0 16 16" aria-hidden="true"><circle cx="8" cy="8" r="8" fill="#fff"/><path d="M5.6 4c.4 0 .6.2.8.6l.6 1.3c.1.3 0 .6-.2.8l-.5.5c.4.9 1.1 1.6 2 2l.5-.5c.2-.2.5-.3.8-.2l1.3.6c.4.2.6.4.6.8v.8c0 .5-.4.9-.9.9C7 11.6 4.4 9 4.4 5.5c0-.5.4-.9.9-.9z" fill="#9e2620"/></svg>
        <span>075 510 203 40</span>
      </li>
      <li class="contact-item">
        <svg viewBox="0 0 16 16" aria-hidden="true"><circle cx="8" cy="8" r="8" fill="#fff"/><g fill="none" stroke="#9e2620" stroke-width="1"><circle cx="8" cy="8" r="4"/><ellipse cx="8" cy="8" rx="1.8" ry="4"/><path d="M4 8h8"/></g></svg>
        <span>www.zum-anker-seedorf.de</span>
      </li>
    </ul>
  </section>

</main>
</body>
</html>
```